Business Card design for new private practice opening

I need a business card design for my new private practice with my new logo uploaded as a file
On the front the logo
On the back: maybe a small logo somewhere?
Priv. Doz. DDr. Corinna Vestaluk
Fachärztin für Allgemein- & Viszeralchirurgie
Address: xxx
Tel: xxx
Mobil:xxx
Webseite:xxx
Email:xxx

Contact Information for Business Card

See project description above for details

Requirements
Nice to have
• I would like the colors of the logo incorporated into the business card

```html
<!DOCTYPE html>
<html lang="de">
<head>
<meta charset="utf-8">
<title>Visitenkarte – Vestaluk Chirurgie</title>
<link rel="stylesheet" href="https://fonts.googleapis.com/css2?family=Inter:wght@400;500;700&display=swap">
<style>
  :root {
    --backdrop: #ececec;
    --card: #ffffff;
    --teal: #5bbdb5;
    --grey: #7d7d7d;
    --ink: #555555;
    --text: #5e5e5e;
  }
  * { margin: 0; padding: 0; box-sizing: border-box; }
  html, body {
    width: 1200px;
    height: 1200px;
    overflow: hidden;
    background: var(--backdrop);
    font-family: "Inter", Arial, sans-serif;
  }
  .sheet {
    position: relative;
    width: 1200px;
    height: 1200px;
  }
  .card {
    position: absolute;
    top: 296px;
    width: 380px;
    height: 606px;
    background: var(--card);
    box-shadow: 0 6px 18px rgba(0, 0, 0, 0.10);
  }
  .card--front { left: 175px; }
  .card--back { left: 646px; }

  /* Front */
  .front-mark {
    position: absolute;
    left: 0;
    right: 0;
    top: 182px;
    display: flex;
    flex-direction: column;
    align-items: center;
    gap: 22px;
  }
  .front-mark__dot {
    width: 200px;
    height: 200px;
    border-radius: 50%;
    background: var(--teal);
  }
  .front-mark__name {
    font-size: 24px;
    font-weight: 500;
    color: var(--grey);
    letter-spacing: 0.02em;
    text-align: center;
    line-height: 1.15;
  }

  /* Back */
  .brand {
    position: absolute;
    left: 40px;
    top: 37px;
    display: flex;
    align-items: center;
    gap: 18px;
  }
  .brand__dot {
    width: 90px;
    height: 90px;
    border-radius: 50%;
    background: var(--teal);
    flex: none;
  }
  .brand__name {
    font-size: 30px;
    font-weight: 500;
    line-height: 1.08;
    color: var(--grey);
    letter-spacing: 0.01em;
  }
  .person {
    position: absolute;
    left: 40px;
    top: 210px;
    right: 30px;
  }
  .person__name {
    font-size: 22px;
    font-weight: 700;
    line-height: 1.3;
    color: var(--ink);
  }
  .person__title {
    margin-top: 8px;
    font-size: 19.5px;
    font-weight: 400;
    line-height: 1.4;
    color: var(--text);
  }
  .contact {
    position: absolute;
    left: 40px;
    top: 422px;
    list-style: none;
    font-size: 20px;
    line-height: 29px;
    color: var(--text);
  }
</style>
</head>
<body>
  <main class="sheet">
    <section class="card card--front" aria-label="Vorderseite">
      <div class="front-mark">
        <div class="front-mark__dot"></div>
        <p class="front-mark__name">VESTALUK<br>CHIRURGIE</p>
      </div>
    </section>

    <section class="card card--back" aria-label="Rückseite">
      <header class="brand">
        <div class="brand__dot"></div>
        <p class="brand__name">VESTALUK<br>CHIRURGIE</p>
      </header>

      <div class="person">
        <h1 class="person__name">Priv. Doz. DDr.<br>Corinna Vestaluk</h1>
        <p class="person__title">Fachärztin für Allgemein-<br>&amp; Viszeralchirurgie</p>
      </div>

      <ul class="contact">
        <li>Address: xxx</li>
        <li>Tel: xxx</li>
        <li>Mobil: xxx</li>
        <li>Webseite: xxx</li>
        <li>Email: xxx</li>
      </ul>
    </section>
  </main>
</body>
</html>
```